Talvon Crest Real estate in need of Logo design

I just started a new real estate brokerage company and need a professional, new logo design that I can incorporate through all forms of marketing and branding. I would like the business card to use both Matte finish and high gloss.

```html
<!DOCTYPE html>
<html lang="en">
<head>
<meta charset="utf-8">
<title>Talvon Crest Real estate – Business Cards</title>
<link href="https://fonts.googleapis.com/css2?family=Montserrat:wght@500;600&family=Work+Sans:wght@400;500&display=swap" rel="stylesheet">
<style>
  :root {
    --gold: #d19f35;
    --gold-light: #dcae4a;
    --charcoal: #58585a;
    --ink: #4a4a4c;
    --paper: #ffffff;
    --backdrop: #e4e4e4;
  }
  * { margin: 0; padding: 0; box-sizing: border-box; }
  html, body { width: 1200px; height: 930px; overflow: hidden; }
  body {
    background: var(--backdrop);
    position: relative;
    font-family: "Work Sans", sans-serif;
  }
  .card {
    position: absolute;
    width: 520px;
    height: 298px;
    border-radius: 22px;
    overflow: hidden;
    box-shadow: 0 6px 18px rgba(0,0,0,0.18);
  }
  .card--front {
    left: 110px;
    top: 120px;
    background: linear-gradient(135deg, var(--gold-light), var(--gold));
    display: flex;
    align-items: center;
    justify-content: center;
  }
  .card--back {
    left: 570px;
    top: 500px;
    background: var(--paper);
  }
  .brand-name {
    font-family: "Montserrat", sans-serif;
    font-weight: 600;
    letter-spacing: 1px;
    text-transform: uppercase;
    text-align: center;
    line-height: 1.2;
  }
  .card--front .brand-name { color: var(--paper); font-size: 26px; }
  .card--back .brand-name { color: var(--gold); font-size: 19px; }
  .brand-mark {
    display: block;
    width: 14px; height: 14px;
    margin: 0 auto 12px;
    background: currentColor;
  }
  .back-brand {
    position: absolute;
    left: 30px;
    top: 0;
    width: 190px;
    height: 286px;
    display: flex;
    flex-direction: column;
    align-items: center;
    justify-content: center;
  }
  .divider {
    position: absolute;
    left: 240px;
    top: 62px;
    width: 2px;
    height: 150px;
    background: var(--gold);
  }
  .contact {
    position: absolute;
    left: 268px;
    top: 54px;
    color: var(--ink);
    font-size: 13.5px;
    line-height: 1.45;
  }
  .contact__name {
    font-family: "Montserrat", sans-serif;
    font-weight: 600;
    font-size: 21px;
    letter-spacing: 1px;
    color: var(--gold);
    text-transform: uppercase;
  }
  .contact__role { font-size: 13px; margin-bottom: 14px; }
  .contact__address { margin-bottom: 14px; }
  .contact__line { display: flex; align-items: center; gap: 8px; }
  .contact__line svg { width: 11px; height: 11px; flex: none; }
  .web-highlight { color: var(--gold); }
  .edge-band {
    position: absolute;
    left: 0; bottom: 0;
    width: 100%;
    height: 12px;
    display: flex;
  }
  .edge-band__grey { width: 58%; background: var(--charcoal); }
  .edge-band__gold { flex: 1; background: var(--gold); }
</style>
</head>
<body>

<section class="card card--front" aria-label="Business card front">
  <div class="brand-name"><span class="brand-mark"></span>Talvon Crest<br>Real estate</div>
</section>

<section class="card card--back" aria-label="Business card back">
  <div class="back-brand">
    <div class="brand-name"><span class="brand-mark"></span>Talvon Crest<br>Real estate</div>
  </div>
  <div class="divider"></div>
  <div class="contact">
    <div class="contact__name">Daren Holloway</div>
    <div class="contact__role">Director</div>
    <div class="contact__address">212b Marlow Lane,<br>Ashford, NZ, 8042</div>
    <div class="contact__line">
      <svg viewBox="0 0 12 12"><path d="M2.5 1 L4.5 1 L5 3.5 L3.8 4.5 Q5 7 7.5 8.2 L8.5 7 L11 7.5 L11 9.5 Q10 11 8 10.8 Q2 9.5 1.2 3.8 Q1 2 2.5 1 Z" fill="#d19f35"/></svg>
      (514) 555-0187
    </div>
    <div class="contact__line">
      <svg viewBox="0 0 12 12"><rect x="1" y="2.5" width="10" height="7" fill="none" stroke="#d19f35" stroke-width="1.2"/><path d="M1 2.5 L6 6.5 L11 2.5" fill="none" stroke="#d19f35" stroke-width="1.2"/></svg>
      info@talvoncrest.com
    </div>
    <div class="contact__line">
      <svg viewBox="0 0 12 12"><circle cx="6" cy="6" r="5" fill="#d19f35"/><path d="M1 6 H11 M6 1 Q3 6 6 11 M6 1 Q9 6 6 11" fill="none" stroke="#fff" stroke-width="0.8"/></svg>
      <span>www.<span class="web-highlight">talvoncrest</span>.com</span>
    </div>
  </div>
  <div class="edge-band">
    <div class="edge-band__grey"></div>
    <div class="edge-band__gold"></div>
  </div>
</section>

</body>
</html>
```